New online business - used mobile phones - needs unique eye catching web design that sets it apart

The Handset Bazaar
We are a new business looking for a rapid response for our web site design. We don't want a normal website....... we need to be creative - most important PLEASE view the attached files uploaded 3 March to ensure you get us :)
.
The Handset Bazaar buys new and damaged mobile phones from the public. A simple process they complete to sell their mobile to us; we want our website to reflect this.
Our website needs to be modern, edgy and fun, not corporate and definitely not like any other mobile phone buying site in the world today!!
Our name was taken from a play on the share/stock market which we have tried to bring into the design ....... it hasn't worked with early designs submitted. Now taking a different approach. Refer to new attached files which should help you visualise our concept.

We like layout from Sketch Flock – rtlbenoviqs #7132809 design as this is very close to our layout vision.
The first page to tell the public what we do, how we do it, and then they click to accept the instant online quote. (page two they complete details about the mobiles model & condition they are selling, then page three complete their personal details).
Our background preference is dark, blackboard or dark with slight texture
a) We love white on black/dark background either typewriter font or look like hand drawn refer to attached files & heronandfig.com.au site to see. Would Label font work???

b) Where the light blue colour is on #7132809 this needs to be like chromavell colour classic green, fern green or bright green, not fluorescent lime green or an insipid green.

c) The banner says The Handset Bazaar is open........... for buying mobiles for cash $$$ (we need people to know we BUY used/damaged phones)

d) We love colour either solid colour or looks like it has been coloured in on our dark background. Open to white or pastel background versions refer to attached coffee file.
We like Chromavell Orange 021,Haute Red,Dazzling Blue, Cyan Blue, Beetroot Purple, Island Green.
e) How it works – underneath this title put Our deal …………. It’s easy as…………..quote, post, get paid!!!
Quote – first circle hand drawn icon showing mobile phone & $ sign. Underneath it says .....Obtain Quote for Model & Condition
Post – second circle hand drawn icon show parcel. Underneath it says Free Post
Paid – third circle hand drawn icon showing large $ sign. Underneath it says Payment in Two Days
Plans - is swapped for wording- Get Market Quote with a large button which says GO or CLICK HERE (they click on the button & it takes them to the next page)
f) FAQ
Allow for six FAQ’s we will forward correct content to you for final design layout.

g) About Us
Please allow about a paragraph of text here, we will forward correct content to you for final design layout.
h) Contact Us
At the bottom where normal website have ………. home, contact details, blog, etc, please only put Email us & Call us, then social media icons for QV, Work Nest and Chirpel

I) LOGO We don’t have one yet, just put The Handset Bazaar at the top & it needs to be large sized font ................we are new and we need to push our name
If you are not clear on our vision ..........please email me and I will reply very quickly.
Thank you for taking the time to read & understand & get us:)

Target Market(s)

20-45 years any body with a spare smart phone that is lying around and they can get cash for. Target market could be slightly older to 50 but focus of 20-40's

Industry/Entity Type

Business

Number of Pages Required

3 page

Font styles to use
Other font styles liked:
• handwritten font or typewriter font

Requirements
Must have
• Read only attached files dated 4 March, tech error with other files, being removed.
• 1 Layout design of Sketch Flock – rtlbenoviqs #7132809
• 2 Hand drawn icons - refer to files
• 3 White font needs to look like hand written refer to heronandfig.com.au or typewriter font - large size font
• 4 Main colours are Black or dark background, green with white text, preference is hand drawn font. The three circles for quote, post & pay with hand drawn icons can be any colour ...... Purple for quote, orange for post & green for paid
• 5 Big green button underneath 3 circles quote/post/pay - customers click on big button to get instant quote
Nice to have
• Coloured in hand drawings as per file
• Great Hand drawings coloured in
Should not have
• NO template designs so it look like you just put some text & a photo. Don't fill the page with mobile phones, one or two is ok, mobile phone pictures date so fast.
• Cartoons

```html
<!DOCTYPE html>
<html lang="en">
<head>
<meta charset="utf-8">
<title>The Handset Bazaar — Sell Your Cell Phone</title>
<link href="https://fonts.googleapis.com/css2?family=Architects+Daughter&family=Open+Sans:wght@400;600;700&display=swap" rel="stylesheet">
<style>
:root{
  --dark:#2e3033;
  --dark-2:#3b3e42;
  --panel:#56595d;
  --panel-line:#74787c;
  --green:#3fd19a;
  --green-deep:#2fb884;
  --white:#ffffff;
  --ink:#3a3a3a;
  --muted:#c9cdd0;
  --hand:"Architects Daughter", cursive;
  --sans:"Open Sans", Arial, sans-serif;
}
*{box-sizing:border-box;margin:0;padding:0}
html,body{width:1200px;height:3276px;overflow:hidden}
body{position:relative;font-family:var(--sans);color:var(--white);background:var(--dark)}
.abs{position:absolute}

/* header + hero */
.hero{position:absolute;left:0;top:0;width:1200px;height:640px;background:radial-gradient(ellipse at 50% 30%,var(--dark-2),var(--dark) 75%)}
.brand{left:40px;top:34px;font-family:var(--sans);font-weight:400;font-size:28px;letter-spacing:1px;text-transform:uppercase}
.nav{left:585px;top:44px;display:flex;gap:34px;font-size:15px;font-weight:600;letter-spacing:.5px}
.btn-start{left:930px;top:32px;width:180px;height:40px;background:var(--green);color:var(--white);font-size:14px;font-weight:700;display:flex;align-items:center;justify-content:center;letter-spacing:.5px}
.hero-photo{left:160px;top:160px;width:150px;height:280px;background:linear-gradient(160deg,#5e6a5a,#1f2224);border-radius:10px}
.sell-panel{left:240px;top:150px;width:840px;height:450px;background:rgba(86,89,93,.97);border:1px solid var(--panel-line);box-shadow:0 10px 40px rgba(0,0,0,.5)}
.sell-panel .close{position:absolute;right:14px;top:8px;color:var(--muted);font-size:22px}
.sell-title{position:absolute;left:0;top:22px;width:100%;text-align:center;font-family:var(--hand);font-size:28px}
.field{position:absolute;left:34px;width:770px;display:flex;justify-content:space-between;align-items:center;font-size:14px}
.select{width:360px;height:32px;background:#3f4245;border:1px solid var(--panel-line);padding:0 12px;display:flex;justify-content:space-between;align-items:center;font-size:14px}
.cond-intro{position:absolute;left:34px;top:250px;font-size:14px}
.cond{position:absolute;left:34px;display:flex;align-items:center;font-size:12px;color:var(--muted)}
.cond b{width:160px;color:var(--white);font-size:19px;font-weight:600;letter-spacing:1px;font-family:var(--hand);padding-left:42px;position:relative}
.cond svg{position:absolute;left:0;top:2px}
.btn-sell{position:absolute;left:640px;top:405px;width:120px;height:32px;border:1px solid var(--white);display:flex;align-items:center;justify-content:center;font-size:13px;font-weight:700}

/* steps */
.steps{position:absolute;left:0;top:640px;width:1200px;height:750px;background:var(--green)}
.step{position:absolute;top:160px;width:300px}
.step h2{font-family:var(--sans);font-weight:700;font-size:30px;display:flex;align-items:center;gap:14px;margin-left:20px}
.step h2 span{width:44px;height:44px;border:2px solid var(--white);border-radius:50%;display:flex;align-items:center;justify-content:center;font-family:var(--hand);font-size:22px}
.step-icon{margin:36px 0 0 40px;width:170px;height:170px;border-radius:50%;background:rgba(255,255,255,.22)}
.step p{margin:26px 0 0 20px;width:240px;text-align:center;font-size:15px;font-weight:600}
.btn-quote{left:490px;top:520px;width:220px;height:54px;border:2px solid var(--white);display:flex;align-items:center;justify-content:center;font-size:15px;font-weight:700;letter-spacing:1px}
.hands{left:0;top:600px;width:1200px;height:150px;background:linear-gradient(180deg,rgba(47,184,132,0),rgba(47,184,132,.9))}

/* about */
.about{position:absolute;left:0;top:1390px;width:1200px;height:540px;background:var(--white)}
.about-photo{left:0;top:0;width:560px;height:540px;background:linear-gradient(120deg,#e9ecea,#c7cfcb 45%,#2c2f31)}
.about h2{position:absolute;left:610px;top:70px;font-family:var(--hand);font-weight:400;font-size:78px;color:var(--green)}
.about p{position:absolute;left:616px;top:215px;width:400px;font-size:14px;line-height:1.5;color:var(--ink)}

/* faq */
.faq{position:absolute;left:0;top:1930px;width:1200px;height:840px;background:radial-gradient(ellipse at 50% 20%,var(--dark-2),#25272a 80%)}
.faq h2{position:absolute;left:0;top:100px;width:100%;text-align:center;font-family:var(--hand);font-weight:400;font-size:56px;letter-spacing:3px}
.faq-item{position:absolute;width:440px}
.faq-item h3{font-size:17px;font-weight:600;color:var(--green);line-height:1.3}
.faq-item .answer{display:flex;gap:16px;margin-top:12px}
.faq-item .answer p{font-size:12.5px;line-height:1.5;color:var(--muted)}

/* contact */
.contact{position:absolute;left:0;top:2770px;width:1200px;height:506px;background:var(--green)}
.contact h2{position:absolute;left:0;top:70px;width:100%;text-align:center;font-family:var(--hand);font-weight:400;font-size:48px}
.input{position:absolute;border:1px solid var(--white);font-size:12px;padding:8px 10px;color:var(--white)}
.btn-send{position:absolute;left:540px;top:305px;width:130px;height:32px;border:1px solid var(--white);display:flex;align-items:center;justify-content:center;font-size:13px;font-weight:700}
.details{position:absolute;left:790px;top:200px;font-size:14px;line-height:1.6}
.follow{position:absolute;left:790px;top:315px;display:flex;align-items:center;gap:10px}
.follow .label{font-family:var(--hand);font-size:26px;margin-right:8px}
.social{display:flex;align-items:center;gap:6px;font-size:13px;font-weight:600}
.social i{width:16px;height:16px;background:var(--white)}
</style>
</head>
<body>

<section class="hero">
  <div class="abs brand">The Handset Bazaar</div>
  <nav class="abs nav"><span>ABOUT US</span><span>FAQ</span><span>CONTACTS</span></nav>
  <div class="abs btn-start">START SELLING ›</div>

  <div class="abs hero-photo" role="img" aria-label="Photo of a phone resting on cash banknotes"></div>

  <form class="abs sell-panel">
    <span class="close">×</span>
    <div class="sell-title">Sell Your Cell Phone</div>
    <div class="field" style="top:78px"><span>Which brand cell phone are you selling?</span><span class="select">Orchard <span>▾</span></span></div>
    <div class="field" style="top:122px"><span>Select your phone series</span><span class="select">Pome Lite <span>▾</span></span></div>
    <div class="field" style="top:166px"><span>Choose the carrier of your device</span><span class="select">please <span>▾</span></span></div>
    <div class="cond-intro">What condition is your product in? <span style="color:var(--muted);font-size:12px;margin-left:10px">Be honest so we can give you the best fair price offer.</span></div>
    <div class="cond" style="top:288px"><b><svg width="28" height="22" viewBox="0 0 28 22"><path d="M2 12 L10 19 L26 2" fill="none" stroke="#fff" stroke-width="2.5" stroke-linecap="round"/></svg>FLAWLESS</b>Works perfectly, no scratches, looks like it came from the box.</div>
    <div class="cond" style="top:326px"><b style="padding-left:82px">GOOD</b>Works fine with light signs of use, small marks on the body or screen.</div>
    <div class="cond" style="top:364px"><b>DAMAGED</b>Cracked, dented or not powering on, we still buy it for parts.</div>
    <div class="btn-sell">SELL</div>
  </form>
</section>

<section class="steps">
  <div class="step" style="left:120px">
    <h2><span>$</span>QUOTE</h2>
    <div class="step-icon" role="img" aria-label="Hand drawn icon of a phone with a dollar sign"></div>
    <p>Obtain quote for model and condition.</p>
  </div>
  <div class="step" style="left:480px">
    <h2><span>✉</span>POST</h2>
    <div class="step-icon" role="img" aria-label="Hand drawn icon of a parcel"></div>
    <p>Free post.</p>
  </div>
  <div class="step" style="left:840px">
    <h2><span>✓</span>GET PAID</h2>
    <div class="step-icon" role="img" aria-label="Hand drawn icon of payment and dollar notes"></div>
    <p>Get payment into your bank account within two days.</p>
  </div>
  <div class="abs btn-quote">GET MARKET QUOTE</div>
  <div class="abs hands" role="img" aria-label="Faint photo of hands holding up phones"></div>
</section>

<section class="about">
  <div class="abs about-photo" role="img" aria-label="Photo of a smiling woman holding out a phone with a greeting on screen"></div>
  <h2>who are we?</h2>
  <p>We are a small team of phone lovers who think old handsets deserve a second life. Instead of sitting in a drawer, your spare phone can earn you cash today. We give honest quotes for every model, cover the postage for you and pay straight into your bank account within two days. Whether the phone is brand new, lightly used or badly cracked, we will make you a fair offer. Simple steps, quick payment and friendly people ready to help whenever you need us.</p>
</section>

<section class="faq">
  <h2>FAQ</h2>
  <div class="faq-item" style="left:120px;top:210px">
    <h3>How much money will I get when I sell my mobile phone for recycling?</h3>
    <div class="answer"><svg width="26" height="22" viewBox="0 0 26 22" style="flex:none"><path d="M2 12 L9 19 L24 2" fill="none" stroke="#fff" stroke-width="2.5" stroke-linecap="round"/></svg><p>The price depends on the model, age and condition. Enter your details in the quote form and you will see your offer straight away, with no hidden fees.</p></div>
  </div>
  <div class="faq-item" style="left:650px;top:210px">
    <h3>How much money will I get when I sell my mobile phone for recycling?</h3>
    <div class="answer"><svg width="26" height="22" viewBox="0 0 26 22" style="flex:none"><path d="M2 12 L9 19 L24 2" fill="none" stroke="#fff" stroke-width="2.5" stroke-linecap="round"/></svg><p>Newer phones in good shape earn the most. Even faulty handsets get a fair offer, as we reuse working parts and recycle the rest safely.</p></div>
  </div>
  <div class="faq-item" style="left:120px;top:400px">
    <h3>How do I send my phone to you once I accept the quote?</h3>
    <div class="answer"><svg width="26" height="22" viewBox="0 0 26 22" style="flex:none"><path d="M2 12 L9 19 L24 2" fill="none" stroke="#fff" stroke-width="2.5" stroke-linecap="round"/></svg><p>We email you a free postage label. Pack the phone safely, attach the label and drop it at any post office near you.</p></div>
  </div>
  <div class="faq-item" style="left:650px;top:400px">
    <h3>Should I remove my SIM card and personal data first?</h3>
    <div class="answer"><svg width="26" height="22" viewBox="0 0 26 22" style="flex:none"><path d="M2 12 L9 19 L24 2" fill="none" stroke="#fff" stroke-width="2.5" stroke-linecap="round"/></svg><p>Yes, please take out your SIM and memory card and reset the phone. We also wipe every device before it goes anywhere.</p></div>
  </div>
  <div class="faq-item" style="left:120px;top:580px">
    <h3>How much money will I get when I sell my mobile?</h3>
    <div class="answer"><svg width="26" height="22" viewBox="0 0 26 22" style="flex:none"><path d="M2 12 L9 19 L24 2" fill="none" stroke="#fff" stroke-width="2.5" stroke-linecap="round"/></svg><p>Your quote is locked for fourteen days. If the phone matches the condition you chose, we pay the full amount you were offered.</p></div>
  </div>
  <div class="faq-item" style="left:650px;top:580px">
    <h3>How much money will I get when I sell my mobile?</h3>
    <div class="answer"><svg width="26" height="22" viewBox="0 0 26 22" style="flex:none"><path d="M2 12 L9 19 L24 2" fill="none" stroke="#fff" stroke-width="2.5" stroke-linecap="round"/></svg><p>Payment goes to your bank account within two days of your phone arriving, and we send you an email as soon as it is done.</p></div>
  </div>
</section>

<section class="contact">
  <h2>contact us!</h2>
  <div class="input" style="left:130px;top:200px;width:250px;height:34px">Your name...</div>
  <div class="input" style="left:130px;top:250px;width:250px;height:34px">Your e-mail...</div>
  <div class="input" style="left:130px;top:300px;width:390px;height:34px">Enter the subject of your message...</div>
  <div class="input" style="left:400px;top:200px;width:270px;height:84px">Your message...</div>
  <div class="btn-send">SEND</div>
  <div class="details">
    (010) 482-7391<br>
    info@handsetbazaar.example<br>
    Larch Avenue, Portmere, PM 000-000
  </div>
  <div class="follow">
    <span class="label">Follow us!</span>
    <span class="social"><i></i>QV</span>
    <span class="social"><i></i>Chirpel</span>
    <span class="social"><i></i>Work Nest</span>
  </div>
</section>

</body>
</html>
```